Ostrel Appraisals BV business cards (a financial services company)

I am looking for a business card design that stands out in the financial advisory field of business & intellectual property valuation. The business card design should be conservative, yet different. Address details have changed since the attached business card. New address is:

Molenvlietkade 27
4817 KT Leiden
The Netherlands

Telephone number remains the same.

```html
<!DOCTYPE html>
<html lang="en">
<head>
<meta charset="utf-8">
<title>Ostrel Appraisals BV — Business Cards</title>
<link href="https://fonts.googleapis.com/css2?family=Cinzel:wght@400;700&family=Libre+Baskerville:wght@400&family=Poppins:wght@400;500&display=swap" rel="stylesheet">
<style>
  :root{
    --bg:#e6e6e6;
    --card:#ffffff;
    --ink:#3d3d3d;
    --ink-soft:#6f6f6f;
    --band:#3b3b3b;
    --on-band:#ffffff;
  }
  *{box-sizing:border-box;margin:0;padding:0}
  html,body{width:1200px;height:800px;overflow:hidden;background:var(--bg)}
  .stage{position:relative;width:1200px;height:800px}
  .card{position:absolute;width:560px;height:320px;background:var(--card);overflow:hidden;
        box-shadow:0 6px 18px rgba(0,0,0,.18)}
  .card--front{left:320px;top:50px}
  .card--back{left:320px;top:430px}
  .card svg.shapes{position:absolute;inset:0}

  /* front */
  .wordmark{position:absolute;left:200px;top:62px;width:304px;height:64px;border:2px solid var(--ink-soft);
            display:flex;align-items:center;justify-content:center;
            font-family:"Cinzel",serif;font-weight:400;font-size:26px;letter-spacing:1px;color:var(--ink-soft)}
  .tagline{position:absolute;left:176px;top:148px;font-family:"Cinzel",serif;color:var(--ink-soft)}
  .tagline__top{font-size:17px;letter-spacing:2.5px;font-weight:400}
  .tagline__bottom{font-size:19px;letter-spacing:2px;font-weight:700;margin-top:2px;padding-left:10px}

  /* back */
  .person{position:absolute;left:38px;top:36px}
  .person__name{font-family:"Libre Baskerville",serif;font-size:27px;color:var(--ink)}
  .person__creds{font-family:"Poppins",sans-serif;font-size:14px;font-weight:500;color:var(--ink-soft);letter-spacing:.5px}
  .person__role{font-family:"Poppins",sans-serif;font-size:13px;color:var(--ink-soft);margin-top:2px}
  .contacts{position:absolute;left:30px;top:112px;list-style:none;font-family:"Poppins",sans-serif;font-size:13px;color:var(--ink-soft)}
  .contacts li{display:flex;align-items:center;gap:12px;height:26px}
  .contacts svg{width:19px;height:19px;flex:none}
  .address{position:absolute;left:20px;top:200px;display:flex;gap:10px;font-family:"Poppins",sans-serif;font-size:13px;line-height:1.35;color:var(--on-band)}
  .address svg{width:16px;height:16px;flex:none;margin-top:1px}
  .mini-mark{position:absolute;right:26px;bottom:22px;font-family:"Cinzel",serif;font-size:14px;letter-spacing:1px;color:var(--ink-soft)}
</style>
</head>
<body>
<main class="stage">

  <section class="card card--front" aria-label="Card front">
    <svg class="shapes" viewBox="0 0 560 320" aria-hidden="true">
      <polygon points="0,108 150,108 158,128 0,128" fill="var(--band)"/>
      <polygon points="410,218 560,218 560,238 404,238" fill="var(--band)"/>
    </svg>
    <div class="wordmark">OSTREL APPRAISALS</div>
    <div class="tagline">
      <p class="tagline__top">BUSINESS AND INTELLECTUAL</p>
      <p class="tagline__bottom">PROPERTY VALUATIONS</p>
    </div>
  </section>

  <section class="card card--back" aria-label="Card back">
    <svg class="shapes" viewBox="0 0 560 320" aria-hidden="true">
      <polygon points="0,188 372,188 392,270 0,270" fill="var(--band)"/>
    </svg>
    <div class="person">
      <p class="person__name">Maarten Velde, <span class="person__creds">CFA, ASA, RV</span></p>
      <p class="person__role">Managing Director</p>
    </div>
    <ul class="contacts">
      <li>
        <svg viewBox="0 0 20 20"><circle cx="10" cy="10" r="10" fill="var(--band)"/><path d="M7 5.5l1.6 2.4-1 1c.6 1.3 1.6 2.3 2.9 2.9l1-1 2.4 1.6-.8 1.6c-3.4-.2-6.5-3.3-6.7-6.7z" fill="#fff"/></svg>
        +31 (0)70 555 0147
      </li>
      <li>
        <svg viewBox="0 0 20 20"><circle cx="10" cy="10" r="10" fill="var(--band)"/><rect x="5" y="6.5" width="10" height="7" fill="#fff"/><path d="M5 6.5l5 4 5-4" fill="none" stroke="var(--band)" stroke-width="1"/></svg>
        mvelde@ostrelappraisals.com
      </li>
      <li>
        <svg viewBox="0 0 20 20"><circle cx="10" cy="10" r="10" fill="var(--band)"/><circle cx="10" cy="10" r="5" fill="none" stroke="#fff" stroke-width="1.2"/><ellipse cx="10" cy="10" rx="2.2" ry="5" fill="none" stroke="#fff" stroke-width="1"/><path d="M5 10h10" stroke="#fff" stroke-width="1"/></svg>
        www.ostrelappraisals.com
      </li>
    </ul>
    <div class="address">
      <svg viewBox="0 0 16 16"><circle cx="8" cy="8" r="8" fill="#fff"/><path d="M8 3.5a3 3 0 0 1 3 3c0 2.2-3 5.8-3 5.8s-3-3.6-3-5.8a3 3 0 0 1 3-3z" fill="var(--band)"/></svg>
      <p>Molenvlietkade 27, 4817 KT Leiden,<br>The Netherlands</p>
    </div>
    <p class="mini-mark">OSTREL</p>
  </section>

</main>
</body>
</html>
```